Corvane Care Group Presentation Folder, for Cancer Awareness, VERY COLORFUL AND MODERN

Presentation Folder I know pretty much what i want so it should be very eazy , I have included files from folders I use now rebrand them to my new company they will be fine, no sense re creating the wheel
Full Bleed Size
20.87" x 16.68"
53 x 42.4 cm
6260 x 5004 pixels
Document Trim Size
20.75" x 16.56"
52.7 x 42.1 cm
6225 x 4969 pixels
Updates

Low design quality

Industry/Entity Type

Medical

Font styles to use
Serif

Colors

Designer to choose colors to be used in the design.

Requirements
Must have
• really I am not looking for some one to redesign, we like our folder front page and would like to see new word information added., there are two folder front pages to choose from
• So Keep the original front page and redesign the back page and the pockets
• Can Make your Design off of one of the ones I already uploaded
Nice to have
• Keep the same color schemes, Keep the original front page and redesign the back page and the pockets
Should not have
• DO not recreate the front covers, use what I gave you and just rebrand

```html
<!DOCTYPE html>
<html lang="en">
<head>
<meta charset="utf-8">
<title>Corvane Care Group – Hereditary Cancer Screening Folder</title>
<link href="https://fonts.googleapis.com/css2?family=Cinzel:wght@500;600;700&family=Bebas+Neue&family=Source+Sans+3:wght@400;600;700&family=Roboto+Condensed:wght@400&display=swap" rel="stylesheet">
<style>
  :root {
    --stage: #808080;
    --navy: #232a66;
    --navy-deep: #1b2150;
    --green: #7fbf3f;
    --pill-text: #f3f0c6;
    --ink: #111111;
    --heading-blue: #2d2f7f;
    --paper: #ffffff;
    --paper-grey: #f4f4f4;
    --serif: "Cinzel", serif;
    --sans: "Source Sans 3", sans-serif;
  }
  * { box-sizing: border-box; margin: 0; padding: 0; }
  html, body { width: 1200px; height: 1200px; overflow: hidden; background: var(--stage); }
  .canvas { position: relative; width: 1200px; height: 1200px; background: var(--stage); font-family: var(--sans); }

  /* Outer spread */
  .outer-spread { position: absolute; left: 160px; top: 78px; width: 800px; height: 506px; overflow: hidden; background: var(--paper); }
  .outer-spread .right-panel { position: absolute; left: 398px; top: 0; width: 402px; height: 506px;
    background: linear-gradient(90deg, #d8d8d8 0%, var(--paper-grey) 30%, var(--paper-grey) 100%); }
  .family-photo { position: absolute; left: 0; top: 252px; width: 398px; height: 254px;
    background: linear-gradient(160deg, #c9d7b4 0%, #e4c9a8 40%, #c2a38b 70%, #7d8fae 100%); }
  .band { position: absolute; left: 0; top: 0; width: 800px; height: 506px; }
  .back-copy { position: absolute; left: 41px; top: 110px; width: 326px; font-size: 9px; line-height: 12.4px; color: var(--ink); text-align: justify; }
  .back-quote { position: absolute; left: 41px; top: 186px; width: 330px; font-size: 13.4px; line-height: 16px; font-weight: 600; color: var(--heading-blue); }
  .brand { display: flex; align-items: center; white-space: nowrap; font-family: var(--serif); font-weight: 600; color: var(--navy); }
  .brand .dot { border-radius: 50%; background: var(--green); flex: none; }
  .back-brand { position: absolute; left: 41px; top: 226px; font-size: 10px; gap: 5px; }
  .back-brand .dot { width: 12px; height: 12px; }

  .cover-title { position: absolute; left: 398px; width: 402px; top: 126px; text-align: center; font-family: var(--serif); color: var(--navy-deep); }
  .cover-title .line-1 { display: block; font-size: 43px; line-height: 44px; font-weight: 700; letter-spacing: 1px; }
  .cover-title .line-2 { display: block; font-size: 28px; line-height: 34px; font-weight: 600; letter-spacing: 0.5px; }
  .gatekeeper-pill { position: absolute; left: 436px; top: 207px; width: 318px; height: 27px; border-radius: 14px; background: var(--green);
    font-family: "Bebas Neue", sans-serif; font-size: 17px; line-height: 28px; color: var(--pill-text); text-align: center; white-space: nowrap; letter-spacing: 0.1px; }
  .cover-intro { position: absolute; left: 444px; width: 310px; top: 241px; text-align: center; font-size: 10px; line-height: 13px; font-weight: 700; color: var(--navy-deep); }
  .cover-brand { position: absolute; left: 398px; width: 402px; top: 316px; justify-content: center; font-size: 21px; gap: 10px; }
  .cover-brand .dot { width: 30px; height: 30px; }
  .cover-tagline { position: absolute; left: 398px; width: 402px; top: 464px; text-align: center; font-size: 10px; color: #ffffff; }

  /* Inner spread */
  .inner-spread { position: absolute; left: 237px; top: 630px; width: 790px; height: 500px; overflow: hidden; background: var(--paper); }
  .inside-left { position: absolute; left: 0; top: 0; width: 395px; height: 334px; background: var(--paper); }
  .inside-left .fold-line { position: absolute; left: 218px; top: 0; width: 1px; height: 334px; background: #e6e6e6; }
  .inside-left .fold-shadow { position: absolute; left: 218px; top: 0; width: 177px; height: 334px;
    background: linear-gradient(90deg, #ffffff 0%, #f7f6f7 45%, #e2e0e2 85%, #bfbdbf 100%); }
  .awareness-ribbon { position: absolute; left: 137px; top: 112px; width: 124px; height: 172px;
    background: linear-gradient(135deg, #8d6bb3 0%, #4cb8e6 45%, #b79ad0 100%); border-radius: 4px; }
  .inside-copy { position: absolute; left: 430px; top: 62px; width: 321px; font-size: 9.8px; line-height: 12.3px; color: var(--ink); text-align: justify; }
  .inside-copy p + p { margin-top: 12px; }
  .inside-headline { position: absolute; left: 430px; top: 246px; width: 330px; font-family: "Roboto Condensed", sans-serif; font-size: 17px; line-height: 21px; color: var(--ink); }
  .pockets { position: absolute; left: 0; top: 0; width: 790px; height: 500px; }
  .pocket-brand { position: absolute; left: 40px; width: 260px; top: 414px; justify-content: center; font-size: 17px; color: #ffffff; gap: 8px; }
  .pocket-brand .dot { width: 20px; height: 20px; background: #ffffff; }
  .card-slot { position: absolute; left: 539px; top: 360px; width: 151px; height: 102px; background: var(--paper);
    display: flex; align-items: center; justify-content: center; text-align: center; font-size: 13.5px; line-height: 18px; color: var(--ink); }
  .card-slot .tab { position: absolute; width: 20px; height: 2px; background: #1a1a1a; }
  .card-slot .tab.tl { left: -2px; top: 4px; transform: rotate(-32deg); }
  .card-slot .tab.tr { right: -2px; top: 4px; transform: rotate(32deg); }
  .card-slot .tab.bl { left: -2px; bottom: 4px; transform: rotate(32deg); }
  .card-slot .tab.br { right: -2px; bottom: 4px; transform: rotate(-32deg); }
</style>
</head>
<body>
<div class="canvas">

  <section class="outer-spread">
    <div class="right-panel"></div>
    <div class="family-photo" role="img" aria-label="Photo of a smiling three-generation family sitting together outdoors"></div>

    <svg class="band" viewBox="0 0 800 506" aria-hidden="true">
      <defs>
        <linearGradient id="navyTop" x1="0" x2="1"><stop offset="0" stop-color="#1b1f4e"/><stop offset="0.5" stop-color="#262d6a"/><stop offset="1" stop-color="#1b1f4e"/></linearGradient>
      </defs>
      <path d="M0 0 H 800 Q 430 100 0 38 Z" fill="url(#navyTop)"/>
      <path d="M0 38 Q 430 100 800 0 Q 450 100 0 84 Z" fill="var(--green)"/>
      <path d="M0 506 Q 350 395 800 414 V 506 Z" fill="var(--green)"/>
      <path d="M0 506 Q 400 436 800 466 V 506 Z" fill="var(--navy)"/>
    </svg>

    <p class="back-copy">Hereditary cancer screening provides vital information to help people with a strong personal or family history of cancer understand their own risk of developing the disease. With this information, they can take steps to Potentially Prevent Cancer, Delay the Onset of Cancer or Catch it at an Earlier stage when outcomes and survival rates are Better.</p>
    <p class="back-quote">Knowledge is Power and Power Eradicates Fear. When You are Fearless, You Will Make all the Right Choices!</p>
    <div class="brand back-brand"><span class="dot"></span>Corvane Care Group</div>

    <h1 class="cover-title"><span class="line-1">HEREDITARY</span><span class="line-2">CANCER SCREENING</span></h1>
    <div class="gatekeeper-pill">DOCTORS ARE THE GATEKEEPERS TO GENETIC TESTING</div>
    <p class="cover-intro">We have an obligation to help patients understand genetic risk and how testing can guide heath care decisions.</p>
    <div class="brand cover-brand"><span class="dot"></span>Corvane Care Group</div>
    <p class="cover-tagline">The test you order FOR your patients</p>
  </section>

  <section class="inner-spread">
    <div class="inside-left">
      <div class="fold-shadow"></div>
      <div class="fold-line"></div>
      <div class="awareness-ribbon" role="img" aria-label="Blue and purple cancer awareness ribbon"></div>
    </div>

    <div class="inside-copy">
      <p>There are many benefits to getting tested, regardless of the eventual result. If one of your family members — however distant — had cancer, there is a chance that you inherited a gene mutation that not only increases your personal risk of cancer, but also could be passed to the next generation. Those who are carriers of hereditary cancer gene mutations, could be at risk of getting cancer earlier in life than the general population. The sooner genetic testing is done, the more likely it is that the risk can be managed appropriately.</p>
      <p>Hereditary cancer screening provides vital information to help people with a strong personal or family history of cancer understand their own risk of developing the disease. With this information, they can take steps to Potentially Prevent Cancer, Delay the Onset of Cancer or Catch it at an Earlier stage when outcomes and survival rates are Better.</p>
    </div>
    <p class="inside-headline">Identifying an inherited genetic mutation has the potential to prevent cancer and save lives.</p>

    <svg class="pockets" viewBox="0 0 790 500" aria-hidden="true">
      <defs>
        <linearGradient id="pocketFill" x1="0" x2="1"><stop offset="0" stop-color="#1b2c5c"/><stop offset="0.5" stop-color="#24396f"/><stop offset="1" stop-color="#1b2c5c"/></linearGradient>
      </defs>
      <path d="M0 334 H 362 Q 375 334 376 348 L 395 500 H 0 Z" fill="url(#pocketFill)"/>
      <path d="M790 334 H 432 Q 419 334 416 348 L 395 500 H 790 Z" fill="url(#pocketFill)"/>
    </svg>

    <div class="brand pocket-brand"><span class="dot"></span>Corvane Care Group</div>
    <div class="card-slot">
      <span class="tab tl"></span><span class="tab tr"></span><span class="tab bl"></span><span class="tab br"></span>
      Space for<br>Business card
    </div>
  </section>

</div>
</body>
</html>
```